Kelmori.com.au - AV and Communications Installation Company Website

A company website for a modern, high level/enterprise communications installation/engineering company based in Sydney Australia.
My client base is construction companies working in medical, government and educations departments so the website needs to look professional.
Clients like Brisle or Torvex as I want to eventually move into data centre design and installation so I need something appealing to the high end market.
Fiber Optic Installation is a massive part of the company aswell.
Audio visual, IT installation is also what the company will be involved in.
I want the website to be modern, eye catching, professional looking.

Target Market(s)

High end clients and construction companies

Industry/Entity Type

Communications

Coding

Coded - Design and coding required

Number of Pages Required

1 page

Requirements
Must have
• Modern and clean layout with links to other social media platforms

```html
<!DOCTYPE html>
<html lang="en">
<head>
<meta charset="utf-8">
<title>Kelmori — AV &amp; Communications Installation</title>
<link rel="stylesheet" href="https://fonts.googleapis.com/css2?family=Montserrat:wght@400;500;600;700&display=swap">
<style>
:root{
  --ink:#0a1a1c;
  --ink-deep:#07151a;
  --teal:#1aa2b4;
  --teal-btn:#1c93a3;
  --teal-soft:#1c8f9c;
  --form-bg:#153a3c;
  --field:#1e5052;
  --field-text:#2b9aa6;
  --white:#ffffff;
  --muted:#b9c6c8;
  --rule:#1b3236;
}
*{margin:0;padding:0;box-sizing:border-box}
html,body{width:1200px;height:3286px;overflow:hidden}
body{position:relative;background:var(--ink);font-family:'Montserrat',sans-serif;color:var(--white)}
.abs{position:absolute}

/* header */
.site-nav{left:0;top:0;width:1200px;height:60px;z-index:5}
.brand{left:176px;top:14px;display:flex;align-items:center;gap:8px;font-size:32px;font-weight:500;color:var(--teal-soft);letter-spacing:1px}
.brand-mark{width:14px;height:14px;background:var(--teal-soft)}
.nav-links{left:529px;top:22px;font-size:11px;font-weight:500;color:#1f2a2c;letter-spacing:.2px}
.nav-links span{position:absolute;white-space:nowrap}
.quote-btn{left:935px;top:17px;width:85px;height:26px;background:var(--teal-btn);color:var(--white);font-size:10px;font-weight:500;display:flex;align-items:center;justify-content:center;border-radius:2px}

/* hero */
.hero-photo{left:0;top:0;width:1200px;height:1010px;background:linear-gradient(110deg,#5e5650 0%,#4a433e 25%,#b7b3ac 45%,#d9d6d0 60%,#8b8f93 80%,#5d5f63 100%)}
.hero-accent{left:540px;top:90px;width:360px;height:230px;border-radius:50%;background:radial-gradient(ellipse,#f2c12a 0%,rgba(242,193,42,0) 70%)}
.hero-fade{left:0;top:620px;width:1200px;height:390px;background:linear-gradient(to bottom,rgba(10,26,28,0) 0%,rgba(10,26,28,.75) 55%,var(--ink) 100%)}
.welcome{left:242px;top:641px;width:716px;height:239px;background:var(--teal);border-radius:3px;text-align:center}
.welcome h1{margin-top:42px;font-size:29px;font-weight:500;letter-spacing:.5px}
.welcome p{margin:12px auto 0;width:460px;font-size:15px;line-height:22px;font-weight:400}
.welcome .btn{display:inline-block;margin-top:28px;width:118px;height:34px;line-height:34px;background:var(--white);color:var(--teal);font-size:11px;font-weight:700;border-radius:2px;letter-spacing:.3px}

/* section titles */
.eyebrow{width:1200px;left:0;text-align:center;font-size:11px;letter-spacing:5px;color:var(--teal);font-weight:500}
.section-title{width:1200px;left:0;text-align:center;font-size:23px;font-weight:500;letter-spacing:.5px}

/* cards */
.card{width:267px;height:304px;border-radius:4px;overflow:hidden}
.card .photo{position:absolute;inset:0}
.card .shade{position:absolute;left:0;bottom:0;width:100%;height:140px;background:linear-gradient(to bottom,rgba(0,0,0,0),rgba(0,0,0,.7))}
.card h3{position:absolute;left:0;bottom:30px;width:100%;text-align:center;font-size:18px;font-weight:600;letter-spacing:.5px}
.card .more{position:absolute;left:0;bottom:7px;width:100%;text-align:center;font-size:13px;color:#e6ecec}

/* about */
.about-photo{border-radius:4px}
.about-ghost{left:609px;top:1508px;font-size:52px;font-weight:700;color:#1e2e31;letter-spacing:1px}
.about-tag{left:631px;top:1541px;font-size:11px;color:var(--white)}
.about-heading{left:636px;top:1580px;font-size:23.5px;line-height:30.5px;font-weight:400;white-space:nowrap}
.about-text{left:638px;top:1727px;font-size:11px;line-height:19.6px;color:var(--muted);white-space:nowrap}
.outline-btn{left:639px;top:1851px;width:106px;height:36px;border:1px solid var(--teal);border-radius:2px;font-size:11.5px;display:flex;align-items:center;justify-content:center}

/* contact form */
.form-panel{left:372px;top:2582px;width:455px;height:399px;background:var(--form-bg);border-radius:4px}
.field{height:33px;background:var(--field);font-size:10px;color:var(--field-text);padding:11px 12px}
.submit{left:547px;top:2901px;width:106px;height:35px;background:var(--teal-btn);font-size:12px;display:flex;align-items:center;justify-content:center;border-radius:2px}

/* footer */
.footer{left:0;top:3042px;width:1200px;height:244px;background:var(--ink-deep)}
.foot-head{top:3086px;font-size:14.5px;font-weight:500}
.foot-rule{top:3110px;width:36px;height:2px;background:var(--teal)}
.foot-about{left:178px;top:3133px;font-size:9.4px;line-height:16.6px;color:var(--muted);white-space:nowrap}
.foot-list{list-style:none;font-size:10.5px;color:var(--muted)}
.foot-list li{height:25.5px;display:flex;align-items:center;gap:9px}
.foot-list li::before{content:"";width:4px;height:4px;background:var(--muted)}
.contact-list{left:817px;top:3130px;list-style:none;font-size:11px;color:var(--muted)}
.contact-list li{height:30px;display:flex;align-items:center;gap:11px}
.contact-list svg{width:12px;height:12px;fill:var(--muted)}
.foot-divider{left:0;top:3242px;width:1200px;height:1px;background:var(--rule)}
.copyright{left:0;top:3257px;width:1200px;text-align:center;font-size:11px;color:var(--muted)}
</style>
</head>
<body>

<!-- hero -->
<div class="abs hero-photo" role="img" aria-label="Two engineers in yellow hard hats working at a communications cabinet"></div>
<div class="abs hero-accent"></div>
<div class="abs hero-fade"></div>

<header class="abs site-nav">
  <div class="abs brand"><span class="brand-mark"></span>Kelmori</div>
  <nav class="abs nav-links">
    <span style="left:0">HOME</span>
    <span style="left:59px">ABOUT US</span>
    <span style="left:143px">SERVICES</span>
    <span style="left:222px">OUR WORK</span>
    <span style="left:311px">CONTACT US</span>
  </nav>
  <div class="abs quote-btn">GET A QUOTE</div>
</header>

<section class="abs welcome">
  <h1>WELCOME TO KELMORI</h1>
  <p>Lorem Ipsum is simply dummy text of the printing and typesetting industry. Lorem Ipsum.</p>
  <span class="btn">OUR SERVICES</span>
</section>

<!-- services -->
<div class="abs eyebrow" style="top:978px">OUR</div>
<h2 class="abs section-title" style="top:997px">SERVICES</h2>

<article class="abs card" style="left:177px;top:1062px">
  <div class="photo" role="img" aria-label="Blue fibre optic patch panel with yellow cables" style="background:linear-gradient(135deg,#1d6fd0,#2a8ae0 45%,#c9b43a 75%,#e1c84a)"></div>
  <div class="shade"></div><h3>IT Installation</h3><div class="more">Read More</div>
</article>
<article class="abs card" style="left:467px;top:1062px">
  <div class="photo" role="img" aria-label="Row of electrical circuit breakers" style="background:linear-gradient(180deg,#d9dde0,#9aa1a6 50%,#4a5056)"></div>
  <div class="shade"></div><h3>IT Installation</h3><div class="more">Read More</div>
</article>
<article class="abs card" style="left:756px;top:1062px">
  <div class="photo" role="img" aria-label="Worker in high-visibility vest beside a cable-laying machine" style="background:linear-gradient(160deg,#cfe0ee,#c9b88a 40%,#d2622c 55%,#8a7c66)"></div>
  <div class="shade"></div><h3>IT Installation</h3><div class="more">Read More</div>
</article>

<!-- about -->
<div class="abs about-photo" role="img" aria-label="Red network switch in a server rack" style="left:219px;top:1499px;width:288px;height:100px;background:linear-gradient(100deg,#c0302a,#d9b070 45%,#c9c4bb)"></div>
<div class="abs about-photo" role="img" aria-label="Hand connecting yellow fibre cables" style="left:264px;top:1623px;width:287px;height:100px;background:linear-gradient(100deg,#2b2a28,#d6a64a 45%,#e0b68e 70%,#7d776f)"></div>
<div class="abs about-photo" role="img" aria-label="Yellow fibre patch cables in a rack" style="left:177px;top:1746px;width:287px;height:99px;background:linear-gradient(100deg,#d8b83a,#2a2a28 45%,#e0c24a 75%,#cfcac2)"></div>

<div class="abs about-ghost">ABOUT</div>
<div class="abs about-tag">[ ABOUT US ]</div>
<h2 class="abs about-heading">Kelmori are a highly skilled engineering<br>organisation operating throughout<br>NSW across all sectors of the construction<br>and services industries.</h2>
<p class="abs about-text">Lorem Ipsum is simply dummy text of the printing and typesetting<br>industry. Lorem Ipsum has been the industry's standard dummy<br>text ever since the 1500s, when an unknown printer took a galley of<br>type and scrambled it to make a type specimen book. It has<br>survived not only five centuries,.</p>
<div class="abs outline-btn">Read More</div>

<!-- projects -->
<div class="abs eyebrow" style="top:2008px">RECENT</div>
<h2 class="abs section-title" style="top:2027px">PROJECTS</h2>

<article class="abs card" style="left:177px;top:2092px">
  <div class="photo" role="img" aria-label="Technician with laptop working at a server cabinet" style="background:linear-gradient(150deg,#e8e8e6,#bfc2c4 40%,#34466a 60%,#5a5a5a)"></div>
  <div class="shade"></div><h3>Lorem Ipsum is simply</h3><div class="more">Read More</div>
</article>
<article class="abs card" style="left:467px;top:2092px">
  <div class="photo" role="img" aria-label="Electrician with tool belt beside a work van" style="background:linear-gradient(170deg,#c9ccd0,#5b5f66 45%,#3a3d42)"></div>
  <div class="shade"></div><h3>Established fact that</h3><div class="more">Read More</div>
</article>
<article class="abs card" style="left:756px;top:2092px">
  <div class="photo" role="img" aria-label="Two engineers with a laptop in a data centre" style="background:linear-gradient(150deg,#3b4654,#8c96a2 45%,#d8dde2 65%,#3c4450)"></div>
  <div class="shade"></div><h3>Simply dummy text</h3><div class="more">Read More</div>
</article>

<!-- contact -->
<div class="abs eyebrow" style="top:2503px">REACH OUT</div>
<h2 class="abs section-title" style="top:2522px">COMMENTS &amp; QUESTIONS?</h2>

<form class="abs form-panel" aria-label="Contact form"></form>
<div class="abs field" style="left:395px;top:2625px;width:194px">First Name</div>
<div class="abs field" style="left:613px;top:2625px;width:194px">Last Name</div>
<div class="abs field" style="left:395px;top:2676px;width:194px">Email Address</div>
<div class="abs field" style="left:613px;top:2676px;width:194px">Phone Number</div>
<div class="abs field" style="left:395px;top:2728px;width:412px">Select Location</div>
<div class="abs field" style="left:395px;top:2781px;width:409px;height:90px">Message</div>
<div class="abs submit">SUBMIT</div>

<!-- footer -->
<footer class="abs footer"></footer>
<div class="abs foot-head" style="left:176px">Kelmori.com.au</div>
<div class="abs foot-rule" style="left:176px"></div>
<p class="abs foot-about">Lorem Ipsum is simply dummy<br>text of the printing and typesetting<br>industry. Lorem Ipsum has been<br>the industry's standard dummy<br>text ever since the 1500s, when</p>

<div class="abs foot-head" style="left:385px">Services</div>
<div class="abs foot-rule" style="left:385px"></div>
<ul class="abs foot-list" style="left:385px;top:3130px">
  <li>Fiber Optic Installation</li><li>Audio Visual</li><li>IT Installation</li>
</ul>

<div class="abs foot-head" style="left:602px">Follow Us</div>
<div class="abs foot-rule" style="left:602px"></div>
<ul class="abs foot-list" style="left:602px;top:3130px">
  <li>Circlepage</li><li>Chirpline</li><li>Snapframe</li>
</ul>

<div class="abs foot-head" style="left:817px">Contact Info</div>
<div class="abs foot-rule" style="left:817px"></div>
<ul class="abs contact-list">
  <li><svg viewBox="0 0 12 12"><rect x="0" y="2" width="12" height="8"/></svg>info@kelmori.com.au</li>
  <li><svg viewBox="0 0 12 12"><path d="M2 0l3 3-1.5 1.5a7 7 0 0 0 4 4L9 7l3 3-2 2C4 12 0 8 0 2z"/></svg>000-555-0147</li>
  <li><svg viewBox="0 0 12 12"><circle cx="6" cy="6" r="6"/></svg>www.kelmori.com.au</li>
</ul>

<div class="abs foot-divider"></div>
<div class="abs copyright">©&nbsp; Copyright 2020 All Right Reserved.</div>

</body>
</html>
```